Schulungen und Brandschutzdienstleistungen
Zielgruppe
Wir sind im vorbeugenden und organisatorischen Brandschutz tätig. Unsere Zielgruppe sind Firmen die Unterstützung, Beratung und die Schulung Ihrer Mitarbeiter beötigen.
Aufgabenstellung
Vorgaben ergeben sich aus dem Design der Homepage und dem pdf Upload (Beispiel des letzten Flyers).
Es sollen die Schulungsleistungen wie Brandschutzhelfer, Erste Hilfe und Unterweisungen hervorgehoben werden. Weiterhin sollen unsere Dienstleistungen, insbesondere der externe Brandschutzbeauftragte, aufgezeigt werden.
Schön währe auf der letzten Seite ein Anmeldeformular für die Schulungen.
Texte und Logo dürfen gerne verwendet werden.
Die Flyer soll zusammen mit einem Anschreiben in eine DIN lang Briefumschlag passen.

```html
<!DOCTYPE html>
<html lang="de">
<head>
<meta charset="utf-8">
<title>Brandschutz Kolbeck – Flyer Schulungen und Dienstleistungen</title>
<link href="https://fonts.googleapis.com/css2?family=Comfortaa:wght@500;700&family=Quicksand:wght@400;600;700&display=swap" rel="stylesheet">
<style>
:root{
  --board:#7f7f7f;
  --red:#cd141c;
  --paper:#ffffff;
  --ink:#2b2b2b;
  --rule:#555555;
  --label:#1d1d1d;
}
*{box-sizing:border-box;margin:0;padding:0}
html,body{width:1200px;height:1200px;overflow:hidden}
body{background:var(--board);font-family:"Quicksand",sans-serif;color:var(--ink);position:relative}
.sheet{position:absolute;background:var(--paper);box-shadow:2px 3px 6px rgba(0,0,0,.45)}
.abs{position:absolute}
.label{position:absolute;font-family:"Quicksand",sans-serif;font-weight:700;font-size:19px;color:var(--label)}
.tab{position:absolute;background:var(--red);color:#fff;font-family:"Comfortaa",sans-serif;font-weight:700}
.tab::after{content:"";position:absolute;left:0;top:100%;width:15px;height:15px;background:var(--red);clip-path:polygon(0 0,100% 0,0 100%)}
.photo{position:absolute}
.body{position:absolute;font-size:5.3px;line-height:1.28}
.body p{margin-bottom:5px}
.kicker{color:var(--red);font-weight:700;font-size:5.3px;margin-bottom:5px}
.bullets{list-style:none}
.bullets li{position:relative;padding-left:5px;margin-bottom:2px}
.bullets li::before{content:"";position:absolute;left:0;top:2px;width:2px;height:2px;border-radius:50%;background:var(--red)}
.field{position:absolute;left:20px;width:152px;border-bottom:.7px solid var(--rule);font-size:5.3px;padding-bottom:1px}
.line{position:absolute;left:20px;width:152px;border-bottom:.7px solid var(--rule)}
.contact{position:absolute;color:#fff;font-size:6px;line-height:1.3}
.contact strong{font-weight:700;display:block;margin-bottom:8px}
.badge{position:absolute;width:110px;height:110px;border-radius:50%;background:#fff;display:flex;align-items:center;justify-content:center;text-align:center;font-family:"Comfortaa",sans-serif;font-weight:700;color:var(--red);font-size:13px;line-height:1.15}
.cover-title{position:absolute;color:#fff;font-family:"Comfortaa",sans-serif;font-weight:500;text-align:center;font-size:15px;line-height:1.3;letter-spacing:.3px}
.cover-title .year{display:block;margin-top:6px}
.fire{background:linear-gradient(180deg,#b8a48e 0%,#c9a27a 30%,#e2a450 60%,#f0b45a 100%)}
</style>
</head>
<body>

<!-- Aussenseite -->
<section class="sheet outside" style="left:21px;top:19px;width:742px;height:392px">
  <!-- Anmeldeformular -->
  <div class="tab" style="left:9px;top:9px;width:163px;height:36px;font-size:13px;padding:11px 0 0 16px">Anmeldeformular</div>
  <div class="body" style="left:20px;top:72px;width:152px">Ich möchte mich für folgendes Seminar Anmelden:</div>
  <div class="line" style="top:99px"></div>
  <div class="line" style="top:114px"></div>
  <div class="line" style="top:129px"></div>
  <div class="line" style="top:143px"></div>
  <div class="field" style="top:187px">Name, Vorname</div>
  <div class="field" style="top:210px">Strasse</div>
  <div class="field" style="top:233px">PLZ, Ort</div>
  <div class="field" style="top:257px">E-Mail</div>
  <div class="field" style="top:281px">Telefonnummer</div>
  <div class="abs" style="left:9px;top:347px;width:163px;height:36px;background:var(--red);color:#fff;font-size:5.3px;line-height:1.25;padding:5px 0 0 11px">Schicken Sie dieses Anmeldeformular per Mail an:<br>anmeldung@brandschutz-kolbeck.de<br>oder per Post an Brandschutz Kolbeck,<br>Lindenweg 19, 41460 Musterstadt</div>

  <!-- Erste Hilfe -->
  <div class="tab" style="left:191px;top:9px;width:170px;height:36px;font-size:13px;padding:11px 0 0 16px">Erste Hilfe</div>
  <div class="body" style="left:206px;top:72px;width:154px">
    <div class="kicker">Qualifizierende Ausbildung in Erste Hilfe für Privat, Betrieb und alle Führerscheinklassen.</div>
    <p>Lernen Sie in Notfallsituationen richtig helfen zu können und rüsten Sie sich für den Ernstfall sowohl im privaten als auch im betrieblichen Umfeld.</p>
    <p>Als anerkannte und von den Berufsgenossenschaften ermächtigte Ausbildungsstelle für betriebliche Ersthelfer ist die Übernahme der Ausbildungskosten durch die BG bzw. Unfallversicherungsträger bei uns möglich! Unsere anerkannten Fachdozenten sind alle seit Jahren im Rettungsdienst tätig und vermitteln auf spannender Weise Ihr umfangreiches Fachwissen mit praxisorientierten Fallbeispielen.</p>
    <div class="kicker" style="margin-top:8px">Wir bieten Seminare für:</div>
    <ul class="bullets">
      <li style="margin-bottom:6px">Betrieblicher Ersthelfer</li>
      <li style="margin-bottom:6px">Erste Hilfe in Bildungs- und Betreuungseinrichtungen für Kinder</li>
      <li>Erste Hilfe für Führerscheine</li>
    </ul>
  </div>
  <div class="photo" role="img" aria-label="Foto: roter Erste-Hilfe-Koffer mit Teddybär und Verbandsmaterial" style="left:202px;top:255px;width:156px;height:128px;background:radial-gradient(ellipse at 50% 45%,#f0542a 0%,#e8643a 35%,#f3e7dc 70%,#fafafa 100%)"></div>

  <!-- Titelseite im Verbund -->
  <div class="abs" style="left:376px;top:9px;width:357px;height:374px;overflow:hidden">
    <div class="photo fire" role="img" aria-label="Foto: grünes Notausgangsschild an der Decke hinter Flammen" style="left:0;top:0;width:357px;height:260px"></div>
    <svg class="abs" style="left:0;top:0" width="357" height="374" viewBox="0 0 357 374"><polygon points="0,255 292,255 357,187 357,374 0,374" fill="#cd141c"/></svg>
    <div class="contact" style="left:9px;top:268px">
      <strong>So erreichen Sie uns</strong>
      Brandschutz Kolbeck<br>Lena Hartwig<br>Lindenweg 19<br>41460 Musterstadt<br>(02131) 5550182<br>info@brandschutz-kolbeck.de<br><br>
      Besuchen Sie uns im Web:<br>www.brandschutz-kolbeck.de<br>Seminare und Schulungen auch online buchbar
    </div>
    <div class="badge" style="left:212px;top:186px">Brandschutz<br>Kolbeck</div>
    <div class="cover-title" style="left:187px;top:302px;width:160px">Schulungen und<br>Dienstleistungen<span class="year">2017</span></div>
  </div>
</section>
<div class="label" style="left:60px;top:432px">aussen kompett aufgeklappt</div>

<!-- Titel -->
<section class="sheet title-card" style="left:871px;top:22px;width:188px;height:393px">
  <div class="abs" style="left:0;top:9px;width:179px;height:374px;overflow:hidden">
    <div class="photo fire" role="img" aria-label="Foto: Notausgangsschild hinter Flammen" style="left:0;top:0;width:179px;height:260px"></div>
    <svg class="abs" style="left:0;top:0" width="179" height="374" viewBox="0 0 179 374"><polygon points="0,255 135,255 179,187 179,374 0,374" fill="#cd141c"/></svg>
    <div class="badge" style="left:34px;top:186px">Brandschutz<br>Kolbeck</div>
    <div class="cover-title" style="left:4px;top:302px;width:171px">Schulungen und<br>Dienstleistungen<span class="year">2017</span></div>
  </div>
</section>
<div class="label" style="left:869px;top:432px">Titel</div>

<!-- Innenseite -->
<section class="sheet inside" style="left:21px;top:518px;width:748px;height:396px">
  <!-- Brandschutzhelfer -->
  <div class="photo" role="img" aria-label="Foto: zwei Männer bei einer Löschübung an einer Brandwanne" style="left:9px;top:9px;width:172px;height:114px;background:linear-gradient(180deg,#4a4a4c 0%,#6e655c 50%,#d98a3c 80%,#a9a4a0 100%)"></div>
  <div class="tab" style="left:9px;top:123px;width:172px;height:32px;font-size:13px;text-align:center;padding-top:10px">Brandschutzhelfer</div>
  <div class="body" style="left:24px;top:172px;width:156px">
    <p>Nach dem Arbeitsschutzgesetz (§10 ArbSchG – Erste Hilfe und sonstige Notfallmaßnahmen) und den Vorschriften der Berufsgenossenschaften ist jeder Arbeitgeber verpflichtet, in angemessenen Zeitabständen seine Mitarbeiter für das richtige Verhalten im Brandfall zu schulen. Seit 01.01.2013 ist die Arbeitsstätten-Regel ASR A2.2 – Maßnahmen gegen Brände, gültig. Darin wird die Zahl der Brandschutzhelfer auf mindestens 5% der Arbeitnehmer festgelegt. Die Feuerversicherer haben dies größtenteils zu Ihren Versicherungsbedingung gemacht.</p>
    <div class="kicker">Sind Ihre Mitarbeiter ausreichend für den Brand vorbereitet?</div>
    <p>Was nützt Ihnen die Anschaffung gesetzlich vorgeschriebener Feuerlöscher oder Selbsthilfeeinrichtungen, wenn im Ernstfall keiner mit den Geräten umgehen kann. Laut einer Umfrage des Fachverband Betrieblicher Brandschutz e.V. haben 69% aller Befragten noch nie an einer Brandschutzschulung aktiv teilgenommen (siehe Abbildung rechts).</p>
    <p>Daher veranstalten wir <b style="color:var(--red)">Seminare für Brandschutzhelfer.</b></p>
  </div>

  <!-- Externer Brandschutzbeauftragter -->
  <div class="abs" style="left:199px;top:9px;width:357px;height:57px;background:var(--red);color:#fff;font-family:'Comfortaa',sans-serif;font-weight:700;font-size:13px;line-height:1.3;padding:14px 0 0 6px">Externer<br>Brandschutzbeauftragter</div>
  <div class="photo" role="img" aria-label="Foto: Rauchmelder in rötlich-weißem Rauch" style="left:199px;top:66px;width:171px;height:92px;background:radial-gradient(circle at 55% 50%,#e24a3e 0%,#d98c8a 35%,#c9b6be 65%,#8f6a7a 100%)"></div>
  <div class="body" style="left:199px;top:172px;width:168px">
    <p>Für den Brandschutz in Betrieben sind aufgrund besonderer Rechtsvorschriften, behördlichen Auflagen oder Gefährdungsbeurteilungen Brandschutzbeauftragte erforderlich, die durch ihre qualifizierte Ausbildung dem Unternehmer/Arbeitgeber als zentraler Partner für brandschutzrelevante Themen zur Verfügung stehen.</p>
    <p>Je nach Unternehmensgröße ist es effizienter und wirtschaftlicher, diese Aufgabe einem erfahrenen, externen Brandschutzbeauftragten zu übertragen um einen ganzheitlichen Brandschutz im Unternehmen gewährleisten zu können.</p>
    <p>Wir übernehmen für Sie als Unternehmer oder Betreiber einer Immobilie die Funktion des Brandschutzbeauftragten. Nutzen Sie die Vorteile von aktuellem Fachwissen und umfangreichen Erfahrungen im vorbeugenden, organisatorischen und abwehrenden Brandschutz.</p>
    <div class="kicker">Weitere Vorteile auf einem Blick:</div>
    <ul class="bullets">
      <li>Alle wichtigen Aufgaben des Brandschutzes werden zentral wahrgenommen und bieten Ihnen somit die notwendige Sicherheit.</li>
      <li>Ihre Mitarbeiter stehen Ihnen weiterhin für Ihre regulären Aufgaben zur Verfügung.</li>
      <li>Ihnen entstehen keine Kosten für Weiterbildung, Fortbildung und den damit verbundenen Betriebsausfall Ihrer Mitarbeiter.</li>
      <li>Ein externer Brandschutzbeauftragter verhindert innerbetriebliche Spannungen, da die Lösungen für etwaige Probleme neutral und sachbezogen erfolgen können.</li>
      <li>Durch einen externen Brandschutzbeauftragten wird der „Betriebsblindheit“ vorgebeugt.</li>
    </ul>
  </div>
  <div class="body" style="left:388px;top:86px;width:168px">
    <p>Wir würden uns sehr freuen, wenn wir die Aufgabe des externen Brandschutzbeauftragen für Sie übernehmen dürfen.</p>
    <div class="kicker" style="margin-top:26px;margin-bottom:14px">Aufgaben eines Brandschutzbeauftragten</div>
    <p>Brandschutzbeauftragte sind die zentrale Ansprechperson für alle Brandschutzfragen im Betrieb. Sie beraten und unterstützen die Arbeitgeberin oder den Arbeitgeber in allen Fragen des vorbeugenden, abwehrenden und organisatorischen Brandschutzes sowie im betrieblichen Notfallmanagement.</p>
  </div>
  <div class="photo" role="img" aria-label="Foto: Feuerlöscher auf einem Aushang „Verhalten im Brandfall“ mit Rauchmelder" style="left:388px;top:204px;width:168px;height:181px;background:linear-gradient(160deg,#3a3a3a 0%,#b8b2ae 30%,#e7e4e2 55%,#f2f0ee 100%)"></div>

  <!-- Leistungen -->
  <div class="photo" role="img" aria-label="Foto: Löschübung mit Feuerlöscher" style="left:574px;top:9px;width:54px;height:56px;background:linear-gradient(180deg,#6a6258,#e8b060)"></div>
  <div class="photo" role="img" aria-label="Foto: roter Feuerlöscher vor grauer Wand" style="left:630px;top:9px;width:109px;height:56px;background:linear-gradient(90deg,#4f4f4f,#9a9a9a 60%,#c23030)"></div>
  <div class="tab" style="left:574px;top:65px;width:165px;height:34px;font-size:13px;padding:11px 0 0 33px">Leistungen</div>
  <div class="body" style="left:608px;top:130px;width:130px">
    <div class="kicker" style="margin-bottom:6px">Unsere Leistungen im Überblick:</div>
    <ul class="bullets">
      <li style="margin-bottom:4.6px">Brandschutzhelfer</li>
      <li style="margin-bottom:4.6px">Brandschutzordnung</li>
      <li style="margin-bottom:4.6px">Brandschutzpläne</li>
      <li style="margin-bottom:4.6px">Brandschutzunterweisungen</li>
      <li style="margin-bottom:4.6px">Erste Hilfe</li>
      <li style="margin-bottom:4.6px">Externer Brandschutzbeauftragter</li>
      <li style="margin-bottom:4.6px">Fachkraft Rauchwarnmelder</li>
      <li style="margin-bottom:4.6px">Feuerwehr-Laufkarten</li>
      <li style="margin-bottom:4.6px">Feuerwehrpläne</li>
      <li>Flucht- und Rettungswegpläne</li>
    </ul>
  </div>
  <div class="photo" role="img" aria-label="Foto: roter Brandmelder an der Wand" style="left:574px;top:274px;width:54px;height:55px;background:linear-gradient(135deg,#8c8c8c,#c8242a 55%,#9a9a9a)"></div>
  <div class="photo" role="img" aria-label="Foto: Berater im Gespräch an einer Wand" style="left:630px;top:274px;width:54px;height:55px;background:linear-gradient(135deg,#b9b4ae,#7c8fb0 60%,#e4e0dc)"></div>
  <div class="photo" role="img" aria-label="Foto: Sprinklerkopf an der Decke" style="left:686px;top:274px;width:53px;height:55px;background:radial-gradient(circle,#c8c4c0,#8a8580)"></div>
  <div class="photo" role="img" aria-label="Foto: Flammen vor einer Tür" style="left:574px;top:331px;width:54px;height:55px;background:linear-gradient(180deg,#f0a030,#c86018 60%,#5a4a3a)"></div>
  <div class="photo" role="img" aria-label="Foto: zwei Berater vor einem Rolltor" style="left:630px;top:331px;width:54px;height:55px;background:linear-gradient(180deg,#6f747a,#9aa3b3 60%,#4f5258)"></div>
  <div class="photo" role="img" aria-label="Foto: rote Notfallausrüstung" style="left:686px;top:331px;width:53px;height:55px;background:linear-gradient(135deg,#7a7a7a,#c0262a 60%,#6a1a1a)"></div>
</section>
<div class="label" style="left:72px;top:944px">innen komplett aufgeklappt</div>

<!-- Rückseite -->
<section class="sheet back-card" style="left:871px;top:521px;width:189px;height:392px">
  <div class="abs" style="left:9px;top:9px;width:180px;height:374px;overflow:hidden">
    <div class="photo fire" role="img" aria-label="Foto: Notausgangsschild hinter Flammen" style="left:0;top:0;width:180px;height:255px"></div>
    <div class="abs" style="left:0;top:255px;width:180px;height:119px;background:var(--red)"></div>
    <div class="contact" style="left:10px;top:266px">
      <strong>So erreichen Sie uns</strong>
      Brandschutz Kolbeck<br>Lena Hartwig<br>Lindenweg 19<br>41460 Musterstadt<br>(02131) 5550182<br>info@brandschutz-kolbeck.de<br><br>
      Besuchen Sie uns im Web:<br>www.brandschutz-kolbeck.de<br>Seminare und Schulungen auch online buchbar
    </div>
  </div>
</section>
<div class="label" style="left:869px;top:932px">Rückseite</div>

</body>
</html>
```